Q-Rolls Business Card

We are a modern retail clothing store. Established in 1994. I need a presentable card that will amaze vendors when given to them.

Front: Logo in middle
Info Side:

Name: Tomas Velder
Cell: 630-812-4463
Work: 630-917-3384 EXT. 417
Email: Tomas@q-rolls-example.com
Website: www.Q-rolls-example.com

Industry/Entity Type

Business

```html
<!DOCTYPE html>
<html lang="en">
<head>
<meta charset="utf-8">
<title>Q-Rolls Business Card</title>
<link rel="stylesheet" href="https://fonts.googleapis.com/css2?family=Jost:wght@300;400;600&display=swap">
<style>
  :root {
    --backdrop: #dcdcdc;
    --paper: #efefef;
    --ink: #0d0d0d;
    --card-dark: #1d1d1d;
    --text-light: #e8e8e8;
    --rule: #8a8a8a;
    --teal-deep: #1f6b5e;
    --teal: #4b9f8f;
    --teal-pale: #8ccabf;
  }
  * { box-sizing: border-box; margin: 0; padding: 0; }
  html, body {
    width: 1200px; height: 900px; overflow: hidden;
    background: var(--backdrop);
    font-family: "Jost", sans-serif;
  }
  .sheet {
    position: relative; width: 1200px; height: 900px;
    display: flex; flex-direction: column; align-items: center; justify-content: center; gap: 40px;
  }
  .card {
    position: relative; width: 630px; height: 360px; overflow: hidden;
    box-shadow: 0 6px 18px rgba(0,0,0,0.18);
  }
  .card--front { background: var(--paper); }
  .card--back { background: var(--card-dark); color: var(--text-light); }

  .facets { position: absolute; inset: 0; width: 100%; height: 100%; }

  .logo-band {
    position: absolute; top: 48px; left: 212px; right: 0; height: 108px;
    background: var(--ink);
    display: flex; align-items: center; padding-left: 32px;
  }
  .logo-name {
    font-weight: 600; font-size: 76px; letter-spacing: 1px;
    color: var(--paper); line-height: 1;
  }

  .accent-strip { position: absolute; top: 0; right: 0; width: 78px; height: 100%; }

  .holder {
    position: absolute; left: 0; width: 232px; top: 0; height: 100%;
    display: flex; align-items: center; justify-content: flex-end; padding-right: 30px;
    font-weight: 300; font-size: 23px; letter-spacing: 0.3px;
  }
  .divider {
    position: absolute; left: 232px; top: 60px; width: 1px; height: 240px;
    background: var(--rule);
  }
  .contact {
    position: absolute; left: 262px; top: 88px;
    list-style: none; font-weight: 300; font-size: 15px; line-height: 1.3;
  }
  .contact li { display: flex; align-items: center; gap: 14px; margin-bottom: 12px; }
  .contact-icon { flex: none; width: 18px; height: 18px; }
</style>
</head>
<body>
<main class="sheet">

  <section class="card card--front" aria-label="Card front">
    <svg class="facets" viewBox="0 0 630 360" role="img" aria-label="Faceted teal geometric pattern">
      <defs>
        <linearGradient id="facetTone" x1="0" y1="0" x2="1" y2="1">
          <stop offset="0" stop-color="var(--teal-pale)"/>
          <stop offset="0.5" stop-color="var(--teal)"/>
          <stop offset="1" stop-color="var(--teal-deep)"/>
        </linearGradient>
      </defs>
      <polygon points="0,70 190,0 250,0 340,180 300,360 0,360" fill="url(#facetTone)"/>
    </svg>
    <div class="logo-band">
      <span class="logo-name">Q-Rolls</span>
    </div>
  </section>

  <section class="card card--back" aria-label="Card back">
    <svg class="accent-strip" viewBox="0 0 78 360" preserveAspectRatio="none" role="img" aria-label="Faceted teal geometric pattern">
      <defs>
        <linearGradient id="stripTone" x1="0" y1="0" x2="0.6" y2="1">
          <stop offset="0" stop-color="var(--teal-deep)"/>
          <stop offset="0.55" stop-color="var(--teal)"/>
          <stop offset="1" stop-color="var(--teal-pale)"/>
        </linearGradient>
      </defs>
      <rect width="78" height="360" fill="url(#stripTone)"/>
    </svg>

    <p class="holder">Tomas Velder</p>
    <div class="divider"></div>

    <ul class="contact">
      <li>
        <svg class="contact-icon" viewBox="0 0 18 18" aria-hidden="true">
          <circle cx="9" cy="9" r="9" fill="var(--text-light)"/>
          <path d="M6 4.5l1.6 2.2-1 1.1c.6 1.3 1.5 2.2 2.7 2.7l1.1-1 2.2 1.6-.9 1.9C8.7 13 5 9.3 4.1 5.4z" fill="var(--card-dark)"/>
        </svg>
        <span>Cell: 630-812-4463<br>Work: 630-917-3384 EXT. 417</span>
      </li>
      <li>
        <svg class="contact-icon" viewBox="0 0 18 18" aria-hidden="true">
          <circle cx="9" cy="9" r="9" fill="var(--text-light)"/>
          <rect x="4.5" y="6" width="9" height="6.5" fill="var(--card-dark)"/>
          <path d="M4.8 6.3L9 9.6l4.2-3.3" fill="none" stroke="var(--text-light)" stroke-width="0.9"/>
        </svg>
        <span>Tomas@q-rolls-example.com</span>
      </li>
      <li>
        <svg class="contact-icon" viewBox="0 0 18 18" aria-hidden="true">
          <circle cx="9" cy="9" r="9" fill="var(--text-light)"/>
          <rect x="4.5" y="5" width="9" height="6" rx="0.6" fill="none" stroke="var(--card-dark)" stroke-width="1.3"/>
          <path d="M7 13.5h4M9 11v2.5" stroke="var(--card-dark)" stroke-width="1.3"/>
        </svg>
        <span>www.Q-rolls-example.com</span>
      </li>
    </ul>
  </section>

</main>
</body>
</html>
```